New Menu Design for edgy barbershop (with bar)

We have a basic graphic for a brand new membership menu. The menu will be located on the wall in our lobby area -- we are planning on making this a very large graphic, but I don't have exact dimensions.

We are a barbershop with a bar & the hottest lady barbers around. We strive to keep a western / saloon feel throughout the barbershop. We cater to mostly a male clientele, so want to have a masculine feel to any creative additions.

I have attached the graphic we started with -- we want to keep the general set up and flow, but are open to your creative brilliance! Our logo is also attached & you can get a good feel for our style on our website: www.ridgelinetrim.example or on our Facebook page: www.facebook.com/ridgelinetrim.

Let me know if you have any questions, or if you need more detail on any of these elements!

A few key details:
- All designs should be horizontal
- The main focus is on the memberships. We want these to pop, and wow customers -- attention should focus on memberships in the graphic, draw the eye in and look glorious.
- We won't look at designs that are too busy or cluttered. Needs to be easy to read & not overwhelming (even with all the information)
- Not too keen on background imagery or color splashes as these make it too complicated. The visual interest should be in how awesome the memberships are!
- Needs to have a clean, masculine feel. Less is more with the background graphics & focus is on getting the info out and drawing people into the awesome memberships we sell.

Target Market(s)

Men 21-65

Font styles to use
Sans Serif

Requirements
Must have
• Masculine feel, western / Saloon theme. Must have all the info included in the graphic slide.
• - Must be Horizontal
• - Must focus on the memberships (need to make the "wow" and drive people to buy them.
Nice to have
• Additional creative elements that really showcase the memberships as awesome!
Should not have
• - No vertical layouts
• - Overly added graphics or background imagery

```html
<!DOCTYPE html>
<html lang="en">
<head>
<meta charset="utf-8">
<title>Ridgeline Trim – Membership Menu</title>
<link href="https://fonts.googleapis.com/css2?family=Alfa+Slab+One&family=Roboto+Slab:wght@300;400&family=Montserrat:wght@600;700&display=swap" rel="stylesheet">
<style>
:root{
  --ink:#1a1a1a;
  --orange:#e8702a;
  --paper:#ffffff;
}
*{margin:0;padding:0;box-sizing:border-box}
html,body{width:1200px;height:846px;overflow:hidden;background:var(--paper)}
.menu{position:relative;width:1200px;height:846px;background:var(--paper);color:var(--ink);font-family:'Montserrat',sans-serif}
.abs{position:absolute;white-space:nowrap}
.heavy{font-family:'Alfa Slab One',serif;text-transform:uppercase;line-height:1}
.thin{font-family:'Roboto Slab',serif;font-weight:300;text-transform:uppercase;line-height:1}
.wide{letter-spacing:.28em}
.price{font-family:'Alfa Slab One',serif;color:var(--orange);font-size:19px;line-height:1}
.desc{font-weight:700;font-size:8.4px;line-height:14px;text-transform:uppercase;letter-spacing:.03em}
.right{text-align:right}
.center{text-align:center}
.rule{position:absolute;height:1.5px;background:var(--ink)}
.brand-name{position:absolute;left:0;width:1200px;top:38px;text-align:center;font-family:'Alfa Slab One',serif;font-size:34px;color:var(--orange);letter-spacing:.04em}
.kid-band{background:var(--ink);color:var(--paper);font-family:'Alfa Slab One',serif;font-size:10px;line-height:17px;height:17px;letter-spacing:.14em;padding:0 6px;text-transform:uppercase}
.step{font-size:7px;letter-spacing:.1em;text-align:center;font-weight:600;line-height:9px}
.step-title{font-family:'Alfa Slab One',serif;font-size:12px;line-height:13px;letter-spacing:.2em;text-align:center;text-transform:uppercase}
.perks-title{font-family:'Alfa Slab One',serif;font-size:20px;line-height:22px;color:var(--orange);background:var(--paper);padding:0 8px}
.perks-line{font-weight:700;font-size:10.5px;line-height:21.5px;text-transform:uppercase;text-align:center;letter-spacing:.04em}
svg text{font-family:'Alfa Slab One',serif}
</style>
</head>
<body>
<main class="menu">

  <div class="brand-name">Ridgeline Trim</div>

  <!-- Left column -->
  <section class="service cowboy-cut">
    <div class="abs thin" style="left:64px;top:118px;font-size:22px">The</div>
    <div class="abs heavy" style="left:46px;top:140px;font-size:25px">Cow</div>
    <div class="abs heavy" style="left:58px;top:164px;font-size:25px">Boy</div>
    <div class="abs thin" style="left:62px;top:189px;font-size:22px">Cut</div>
    <div class="abs price" style="left:214px;top:116px">$25</div>
    <div class="rule" style="left:125px;top:137px;width:125px"></div>
    <div class="abs desc" style="left:125px;top:140px">Our full service cut.<br>Hair cut, hot towel,<br>double trough wash,<br>and straight razor<br>neck shave.</div>
  </section>

  <section class="service terry">
    <div class="abs thin" style="left:46px;top:224px;font-size:20px">The</div>
    <div class="abs heavy wide" style="left:46px;top:246px;font-size:23px">Terry</div>
    <div class="abs price" style="left:214px;top:250px">$17</div>
    <div class="rule" style="left:46px;top:273px;width:204px"></div>
    <div class="abs desc" style="left:46px;top:278px">Haircut, double trough wash,<br>hot towel, and straight razor<br>neck shave.<br>This is for cowboys<br>that haven't been blessed<br>with a full head of hair.<br>We know it's not fair,<br>that's why your price is!</div>
  </section>

  <section class="service little">
    <div class="abs thin" style="left:46px;top:420px;font-size:22px">The</div>
    <div class="abs heavy wide" style="left:46px;top:441px;font-size:22px">Little</div>
    <div class="abs price" style="left:214px;top:444px">$15</div>
    <div class="abs kid-band" style="left:46px;top:467px;width:204px">Cowboy and Cowgirl</div>
    <div class="abs desc" style="left:46px;top:490px">Kids cuts 14 and under hair cut,<br>trough wash, and neck trim.</div>
  </section>

  <section class="service scalp-scrape">
    <div class="abs thin" style="left:46px;top:542px;font-size:20px">The</div>
    <div class="abs heavy" style="left:46px;top:562px;font-size:23px;letter-spacing:.06em">Scalp</div>
    <div class="abs heavy wide" style="left:46px;top:585px;font-size:23px">Scrape</div>
    <div class="abs price" style="left:218px;top:590px">$30</div>
    <div class="abs desc" style="left:46px;top:614px">We will take a not so rusty<br>straight razor and get rid<br>of your carrot top.</div>
  </section>

  <section class="service rough-rider">
    <div class="abs price" style="left:46px;top:682px">$10</div>
    <div class="abs heavy" style="left:46px;top:702px;font-size:22px;letter-spacing:.06em">Rough</div>
    <div class="abs heavy" style="left:46px;top:724px;font-size:22px;letter-spacing:.06em">Rider</div>
    <div class="abs desc" style="left:46px;top:756px">Straight razor back<br>of the neck shave &amp;<br>two beers to keep your<br>trail rides smooth.</div>
  </section>

  <section class="service colorado">
    <div class="abs price center" style="left:200px;width:160px;top:682px">$10</div>
    <div class="abs thin center" style="left:200px;width:160px;top:702px;font-size:14px">The</div>
    <div class="abs heavy center" style="left:200px;width:160px;top:718px;font-size:22px">Colo</div>
    <div class="abs heavy center" style="left:200px;width:160px;top:740px;font-size:22px">Rado</div>
    <div class="abs desc center" style="left:190px;width:180px;top:768px">Electric trim<br>your man bush (beard)<br>just how you like it!</div>
  </section>

  <section class="service eyebrow">
    <div class="abs price right" style="left:350px;width:200px;top:682px">$10</div>
    <div class="abs thin right" style="left:350px;width:200px;top:702px;font-size:24px;letter-spacing:.06em">Eyebrow</div>
    <div class="abs heavy wide right" style="left:350px;width:206px;top:726px;font-size:22px">Wax</div>
    <div class="abs desc right" style="left:350px;width:200px;top:756px">We can wax them<br>both off, one off,<br>or just touch them up.<br>Add on to any cut.</div>
  </section>

  <!-- Middle column -->
  <section class="service cowgirl-cut">
    <div class="abs price" style="left:306px;top:116px">$25</div>
    <div class="rule" style="left:306px;top:137px;width:90px"></div>
    <div class="abs desc right" style="left:250px;width:143px;top:140px">Our ladies cut.<br>Hair cut,<br>trough wash.</div>
    <div class="abs thin" style="left:400px;top:118px;font-size:22px">The</div>
    <div class="abs heavy" style="left:400px;top:140px;font-size:23px">Cowgirl</div>
    <div class="abs thin" style="left:400px;top:164px;font-size:22px">Cut</div>
  </section>

  <section class="service buzzed">
    <div class="abs thin right wide" style="left:350px;width:206px;top:224px;font-size:20px">Buzzed</div>
    <div class="abs price" style="left:306px;top:250px">$22</div>
    <div class="abs heavy wide" style="left:383px;top:246px;font-size:23px">Cowboy</div>
    <div class="rule" style="left:306px;top:273px;width:244px"></div>
    <div class="abs desc" style="left:306px;top:278px;font-size:7.8px">Buzz cut &amp; two beers, for the straight-<br>forward cowboy. Must be 21+ for this bad boy.</div>
  </section>

  <section class="service cowboy-pack">
    <div class="abs price" style="left:306px;top:342px">$35</div>
    <div class="rule" style="left:306px;top:361px;width:90px"></div>
    <div class="abs desc right" style="left:250px;width:143px;top:364px">Cowboy and<br>little cowboy<br>hair cut.</div>
    <div class="abs thin" style="left:400px;top:344px;font-size:20px">The</div>
    <div class="abs heavy" style="left:400px;top:364px;font-size:23px;letter-spacing:.06em">Cowboy</div>
    <div class="abs heavy" style="left:400px;top:387px;font-size:23px;letter-spacing:.06em">Pack</div>
  </section>

  <section class="service razor-fade">
    <div class="abs price" style="left:306px;top:455px">$30</div>
    <div class="rule" style="left:306px;top:476px;width:90px"></div>
    <div class="abs desc right" style="left:250px;width:143px;top:479px">Razor fade,<br>hot towel,<br>double wash.</div>
    <div class="abs thin" style="left:400px;top:457px;font-size:18px;letter-spacing:.08em">Cowboy</div>
    <div class="abs heavy" style="left:400px;top:477px;font-size:22px;letter-spacing:.4em">Razor</div>
    <div class="abs heavy" style="left:400px;top:500px;font-size:22px;letter-spacing:.4em">Fade</div>
  </section>

  <section class="service double-scrape">
    <div class="abs thin right" style="left:350px;width:200px;top:542px;font-size:20px">The</div>
    <div class="abs heavy right" style="left:350px;width:202px;top:562px;font-size:23px;letter-spacing:.06em">Double</div>
    <div class="abs heavy wide right" style="left:350px;width:206px;top:585px;font-size:23px">Scrape</div>
    <div class="abs price" style="left:306px;top:590px">$30</div>
    <div class="abs desc right" style="left:300px;width:250px;top:614px">We will take a not so rusty straight<br>razor and get rid of your winter scruff.<br>A face shave with and against the grain.</div>
  </section>

  <!-- Memberships -->
  <section class="memberships">
    <svg class="abs" style="left:0;top:0" width="1200" height="846" viewBox="0 0 1200 846" aria-hidden="true">
      <g fill="none" stroke="var(--ink)">
        <path stroke-width="1.5" d="M680 125H1128L1158 155V600L1133 625H675L650 600V155Z"/>
        <path stroke-width="1" d="M684 131H1124L1152 159V597L1130 619H678L656 597V159Z"/>
        <path stroke-width="2" d="M676 168l14-12M680 178l4-16M1128 156l14 12M1140 162l4 16"/>
        <path stroke-width="1.5" d="M680 678H1128L1158 702V808H650V702Z"/>
      </g>
      <circle cx="900" cy="121" r="46" fill="var(--paper)" stroke="var(--ink)" stroke-width="2"/>
      <circle cx="900" cy="121" r="38" fill="none" stroke="var(--orange)" stroke-width="3"/>
      <circle cx="900" cy="121" r="21" fill="none" stroke="var(--ink)" stroke-width="1.5"/>

      <!-- Step 1 shapes -->
      <ellipse cx="745" cy="288" rx="52" ry="24" fill="none" stroke="var(--ink)" stroke-width="2"/>
      <text x="745" y="294" text-anchor="middle" font-size="16" fill="var(--orange)">COWBOY</text>
      <path d="M880 270H855V280M925 270H950V280M855 296V306H950V296" fill="none" stroke="var(--ink)" stroke-width="2"/>
      <text x="903" y="275" text-anchor="middle" font-size="9" fill="var(--orange)" font-family="Roboto Slab">LITTLE</text>
      <text x="903" y="296" text-anchor="middle" font-size="16" fill="var(--orange)">COWBOY</text>
      <path d="M1013 268H1108L1060 314Z" fill="none" stroke="var(--ink)" stroke-width="2"/>
      <text x="1060" y="287" text-anchor="middle" font-size="16" fill="var(--orange)">SHAVE</text>

      <!-- Step 2 visits -->
      <line x1="720" y1="400" x2="1088" y2="400" stroke="var(--ink)" stroke-width="1.5"/>
      <g fill="var(--orange)">
        <polygon points="707,400 713.5,389 726.5,389 733,400 726.5,411 713.5,411"/>
        <polygon points="779,400 785.5,389 798.5,389 805,400 798.5,411 785.5,411"/>
        <polygon points="852,400 858.5,389 871.5,389 878,400 871.5,411 858.5,411"/>
        <polygon points="926,400 932.5,389 945.5,389 952,400 945.5,411 932.5,411"/>
        <polygon points="998,400 1004.5,389 1017.5,389 1024,400 1017.5,411 1004.5,411"/>
        <polygon points="1075,400 1081.5,389 1094.5,389 1101,400 1094.5,411 1081.5,411"/>
      </g>
      <g fill="var(--paper)" font-size="14" text-anchor="middle">
        <text x="720" y="406">1</text><text x="792" y="406">2</text><text x="865" y="406">3</text>
        <text x="939" y="406">4</text><text x="1011" y="406">5</text><text x="1088" y="406">6</text>
      </g>

      <!-- Step 3 extras -->
      <g fill="none" stroke="var(--ink)" stroke-width="1.5">
        <path d="M730 503v-8h8M820 495h8v8M730 527v8h8M820 535h8v-8"/>
        <path d="M880 503v-8h8M1072 495h8v8M880 527v8h8M1072 535h8v-8"/>
        <path d="M730 573v-8h8M820 565h8v8M730 597v8h8M820 605h8v-8"/>
        <path d="M880 573v-8h8M1072 565h8v8M880 597v8h8M1072 605h8v-8"/>
      </g>
      <g text-anchor="middle" fill="var(--orange)">
        <text x="779" y="507" font-size="9" font-family="Roboto Slab">FREE</text>
        <text x="779" y="527" font-size="15">BEER</text>
        <text x="980" y="507" font-size="9" font-family="Roboto Slab">UNLIMITED</text>
        <text x="980" y="527" font-size="15">NECK SHAVES</text>
        <text x="779" y="577" font-size="9" font-family="Roboto Slab">EYEBROW</text>
        <text x="779" y="597" font-size="15">WAX</text>
        <text x="980" y="591" font-size="15">COLORADO</text>
      </g>

      <!-- Perks heading rules -->
      <line x1="820" y1="680" x2="846" y2="680" stroke="var(--orange)" stroke-width="2"/>
      <line x1="954" y1="680" x2="980" y2="680" stroke="var(--orange)" stroke-width="2"/>
    </svg>

    <div class="abs step" style="left:650px;width:508px;top:208px">STEP 1</div>
    <div class="abs step-title" style="left:650px;width:508px;top:219px">Choose your service</div>
    <div class="abs step" style="left:650px;width:508px;top:332px">STEP 2</div>
    <div class="abs step-title" style="left:650px;width:508px;top:343px">Choose your visits</div>
    <div class="abs step" style="left:650px;width:508px;top:358px">(IN WEEKS)</div>
    <div class="abs step" style="left:650px;width:508px;top:444px">STEP 3</div>
    <div class="abs step-title" style="left:650px;width:508px;top:455px">Choose your extras</div>
  </section>

  <section class="perks">
    <div class="abs thin center" style="left:650px;width:508px;top:648px;font-size:14px">The</div>
    <div class="abs center" style="left:650px;width:508px;top:668px"><span class="perks-title">PERKS</span></div>
    <div class="abs center" style="left:650px;width:508px;top:692px;font-family:'Roboto Slab',serif;font-size:8px">(INCLUDED WITH ALL MEMBERSHIPS)</div>
    <div class="abs" style="left:650px;width:508px;top:718px">
      <p class="perks-line">Discounts on additional services, products &amp; drinks!</p>
      <p class="perks-line">Reduced rate for private parties &amp; after-hours events!</p>
      <p class="perks-line">Deals for friends &amp; referral bonuses for you!</p>
      <p class="perks-line">Additional specials, invitations &amp; access throughout the year!</p>
    </div>
  </section>

</main>
</body>
</html>
```